Financial Services Consultant needs a business card

We need a business card for a new consulting company based in Melbourne called
"Korvane Metrics". Tagline is Measure, Monitor, Save
We would like to see business card designs that are in line with the minimal style of the website www.korvane-metrics-example.com
The font I have used on the website is Proxima Nova and would like the same or similar font used on the business card with a minimal design in line with the website Two sided with "KORVANE METRICS" MEASURE, MONITOR, SAVE on one side and name, title and contact details on the otther
Updates

Hi All, thanks for your submissions, much appreciated.

I have recently added some colour to my webiste, it is hex #3a7b74 for those that wish to use it
Thanks

Hi all

thanks very much for your design submissions I am very impressed and they are much appreciated.

Interms of general feedback please find below;

Colour: I am trying to stick to a minimal design and colour scheme for my website which is still under construction, up to 3 colours( www.korvane-metrics-example.com) it is currently black and white with a small amount of blue/green but I am open to suggestion/interpretations for a consulting company.

Card: I dont mind if it has rounded edges or straight, I was thinking about using a letterpress card if possible

Detail: the detail on the card will include; Name, Title, Mobile, Personal Email, Business Email,Web,Business Address

Once again thanks for submissions

Industry/Entity Type

Business

```html
<!DOCTYPE html>
<html lang="en">
<head>
<meta charset="utf-8">
<title>Korvane Metrics – Business Card</title>
<link href="https://fonts.googleapis.com/css2?family=Montserrat:wght@400;500;600;700&display=swap" rel="stylesheet">
<style>
  :root {
    --page-bg: #f4f4f4;
    --card-bg: #ffffff;
    --ink: #000000;
    --faint: #e6e6e6;
    --rule: #dcdcdc;
    --front-border: #333333;
    --back-border: #c8c8c8;
    --on-dark: #ffffff;
  }
  * { margin: 0; padding: 0; box-sizing: border-box; }
  html, body {
    width: 1200px;
    height: 420px;
    overflow: hidden;
    background: var(--page-bg);
    font-family: "Montserrat", Arial, sans-serif;
    color: var(--ink);
  }
  .canvas { position: relative; width: 1200px; height: 420px; }

  .card {
    position: absolute;
    top: 34px;
    width: 555px;
    height: 350px;
    background: var(--card-bg);
  }

  /* Front */
  .card-front {
    left: 28px;
    border: 1px solid var(--front-border);
    box-shadow: 0 1px 2px rgba(0,0,0,0.25);
  }
  .front-name {
    position: absolute;
    left: 0; right: 0;
    top: 132px;
    text-align: center;
    font-size: 42px;
    font-weight: 500;
    letter-spacing: 0.5px;
  }
  .front-tagline {
    position: absolute;
    left: 0; right: 0;
    top: 206px;
    text-align: center;
    font-size: 10.5px;
    font-weight: 600;
    letter-spacing: 0.3px;
  }

  /* Back */
  .card-back {
    left: 627px;
    border: 1px solid var(--back-border);
    overflow: hidden;
  }
  .back-brand {
    position: absolute;
    left: 0; right: 0; top: 0;
    height: 194px;
    border-bottom: 1px solid var(--rule);
  }
  .brand-square {
    position: absolute;
    left: 40px;
    top: 86px;
    width: 22px;
    height: 22px;
    background: var(--ink);
  }
  .brand-name {
    position: absolute;
    left: 76px;
    top: 72px;
    font-size: 40px;
    font-weight: 500;
    color: var(--faint);
    white-space: nowrap;
  }
  .contact {
    position: absolute;
    left: 312px;
    top: 220px;
    line-height: 1.2;
  }
  .contact-name { font-size: 16.5px; font-weight: 500; }
  .contact-title,
  .contact-line { font-size: 13px; font-weight: 500; }
  .web-bar {
    position: absolute;
    left: 0; right: 0;
    top: 324px;
    height: 25px;
    background: var(--ink);
    color: var(--on-dark);
    text-align: center;
    font-size: 13px;
    font-weight: 600;
    line-height: 25px;
  }
</style>
</head>
<body>
<main class="canvas">
  <section class="card card-front" aria-label="Card front">
    <h1 class="front-name">KORVANE METRICS</h1>
    <p class="front-tagline">MEASURE , MONITOR , SAVE</p>
  </section>

  <section class="card card-back" aria-label="Card back">
    <div class="back-brand">
      <span class="brand-square"></span>
      <span class="brand-name">Korvane Metrics</span>
    </div>
    <div class="contact">
      <p class="contact-name">FIRST NAME LAST NAME</p>
      <p class="contact-title">TITLE</p>
      <p class="contact-line">Address goes here</p>
      <p class="contact-line">+00-5550100000</p>
    </div>
    <div class="web-bar">www.korvane-metrics-example.com</div>
  </section>
</main>
</body>
</html>
```